Varlow's Electrical & Solar - Business Cards

I want my business card to stand out from the rest. I will provide my business name logo and my icon logo to be implemented onto the card.

On the front of the card, can i have the following. Just make it neat & professional please.

Dean Harrop
varlowselectrical@mailbox-example.net
0491 837 562
ABN: 41 269 507 813
License No. 582146K
FREE QUOTES
24/7 Emergency

On the back of the card, can I have "Our Services" and maybe add the V logo on the back in the background or something. Under "Our Services" I want the following:

LED Lighting Upgrades
Switches & Outlets
Smoke Alarms
Switchboard Upgrades
Fault Finding
Rewiring
New Builds
Test & Tagging
All Electrical Maintenance & Repairs

Can you guys add the instagram logo and next to it, put varlows_electrical

Can you guys also add the facebook logo and next to it put Varlow's Electrical & Solar. Make sure the instagram & facebook icon is in either white, green or black.

Also I have put down double sided, not sure why when i save it, it keeps going to single sided. I need my business card double sided.

New Customers

Dean Harrop varlowselectrical@mailbox-example.net 0491 837 562 ABN: 41 269 507 813 License No. 582146K FREE QUOTES 24/7 Emergency

• must be tidy, professional and appealing

```html
<!DOCTYPE html>
<html lang="en">
<head>
<meta charset="utf-8">
<title>Varlow's Electrical &amp; Solar – Business Cards</title>
<link href="https://fonts.googleapis.com/css2?family=Barlow:wght@400;500;600;700&display=swap" rel="stylesheet">
<style>
  :root {
    --backdrop: #8e8f93;
    --card-black: #060708;
    --card-white: #ffffff;
    --ink: #111111;
    --brand-green: #2fb34a;
    --brand-silver: #d5d8dc;
    --shadow: 0 6px 10px rgba(0,0,0,0.35);
  }
  * { margin: 0; padding: 0; box-sizing: border-box; }
  html, body { width: 923px; height: 1200px; overflow: hidden; }
  body {
    background: var(--backdrop);
    font-family: "Barlow", Arial, sans-serif;
    position: relative;
  }
  .card { position: absolute; width: 760px; height: 434px; box-shadow: var(--shadow); overflow: hidden; }

  /* Front */
  .card-front { left: 76px; top: 85px; background: var(--card-black); }
  .brand-mark { position: absolute; display: block; }
  .card-front .brand-mark { left: 287px; top: 66px; }
  .brand-name {
    position: absolute; text-align: center; white-space: nowrap;
    color: var(--brand-silver); font-weight: 700; text-transform: uppercase;
    line-height: 1;
  }
  .card-front .brand-name { left: 0; right: 0; top: 286px; font-size: 56px; letter-spacing: 4px; }
  .card-front .brand-name .sub { display: block; font-size: 15px; letter-spacing: 7px; margin-top: 6px; }

  /* Back */
  .card-back { left: 64px; top: 618px; background: var(--card-white); }
  .back-panel { position: absolute; left: 0; top: 0; width: 278px; height: 100%; background: var(--card-black); }
  .panel-stripe { position: absolute; background: var(--card-black); }
  .stripe-top { left: 0; top: 0; width: 294px; height: 33px; }
  .stripe-inner { left: 286px; top: 42px; width: 8px; bottom: 0; }
  .card-back .brand-mark { left: 88px; top: 45px; }
  .card-back .brand-name { left: 0; width: 292px; top: 183px; font-size: 34px; letter-spacing: 2px; }
  .card-back .brand-name .sub { display: block; font-size: 10px; letter-spacing: 4px; margin-top: 4px; }
  .social {
    position: absolute; left: 37px; top: 381px; display: flex; align-items: center; gap: 9px;
    color: var(--card-white); font-size: 21px; letter-spacing: 0.3px; white-space: nowrap;
  }
  .social-square { width: 19px; height: 19px; background: var(--card-white); border-radius: 3px; }

  .details { position: absolute; left: 294px; right: 0; top: 0; bottom: 0; text-align: center; color: var(--ink); }
  .details > * { position: absolute; left: 0; right: 0; white-space: nowrap; line-height: 1; }
  .person-name { top: 40px; font-size: 42px; font-weight: 700; letter-spacing: -0.5px; }
  .person-role { top: 88px; font-size: 24px; font-weight: 400; letter-spacing: 6px; }
  .address { top: 141px; font-size: 18px; line-height: 29px; }
  .contact { top: 214px; font-size: 15px; }
  .offer { top: 270px; display: flex; justify-content: center; align-items: center; gap: 10px; font-size: 21px; }
  .offer .rule { width: 38px; height: 1px; background: var(--ink); }
  .offer strong { font-weight: 700; }
  .services { top: 308px; font-size: 11.5px; font-weight: 500; line-height: 21.5px; letter-spacing: 0.2px; }
  .services .dot { margin: 0 3px; }
  .credentials { top: 385px; font-size: 20px; }
  .credentials strong { font-weight: 700; }
</style>
</head>
<body>

<section class="card card-front">
  <svg class="brand-mark" width="186" height="186" viewBox="0 0 186 186" aria-hidden="true">
    <circle cx="93" cy="93" r="86" fill="none" stroke="var(--brand-green)" stroke-width="10"/>
  </svg>
  <p class="brand-name">Varlow's<span class="sub">Electrical &amp; Solar</span></p>
</section>

<section class="card card-back">
  <div class="back-panel"></div>
  <div class="panel-stripe stripe-top"></div>
  <div class="panel-stripe stripe-inner"></div>

  <svg class="brand-mark" width="116" height="116" viewBox="0 0 116 116" aria-hidden="true">
    <circle cx="58" cy="58" r="53" fill="none" stroke="var(--brand-green)" stroke-width="7"/>
  </svg>
  <p class="brand-name">Varlow's<span class="sub">Electrical &amp; Solar</span></p>

  <div class="social">
    <span class="social-square"></span>
    <span>varlows_electrical</span>
  </div>

  <div class="details">
    <h1 class="person-name">DEAN HARROP</h1>
    <p class="person-role">ELECTRICIAN</p>
    <p class="address">27 MARSH CT, EASTBROOK<br>NSW 2180, AUSTRALIA</p>
    <p class="contact">T : 0491 837 562 &nbsp;|&nbsp; E : varlowselectrical@mailbox-example.net</p>
    <div class="offer">
      <span class="rule"></span>
      <span>FREE QUOTES <strong>| 24/7 EMERGENCY</strong></span>
      <span class="rule"></span>
    </div>
    <p class="services">
      LED LIGHTING UPGRADES<span class="dot">•</span>SWITCHES &amp; OUTLETS<span class="dot">•</span>SMOKE ALARMS<br>
      SWITCHBOARD UPGRADES<span class="dot">•</span>FAULT FINDING<span class="dot">•</span>REWIRING<span class="dot">•</span>NEW BUILDS<br>
      TEST &amp; TAGGING<span class="dot">•</span>ALL ELECTRICAL MAINTENANCE &amp; REPAIRS
    </p>
    <p class="credentials"><strong>ABN</strong> 41 269 507 813 | <strong>LICENSE NO.</strong> 582146K</p>
  </div>
</section>

</body>
</html>
```